Gavin Unboxed - Album

Hi all

I am planning on releasing my first album for online distribution shortly. I have chosen the tracks that I want to put in it. You can listen to them through my set "Gavin Unboxed": http://tunehollow.net/thorneg/sets/gavin-unboxed

I am not particularly happy with the name "Gavin Unboxed", so I have created a competition to find a better album name. Anyone is welcome to enter. The best two entries will win a free copy of the album when it comes out:
http://tunehollow.net/thorneg/album-name
The album name competition will end on December 17.
If you have a design idea before that time, feel free to submit that as well as the album name. You can send as many ideas as you like.
After the album name is decided upon, this will be like a normal design competition.
I am planning on distributing the album online through VexaSonic.
According to vexasonic.net: "Submitted cover art must be 1500 x 1500 pixels jpg. It cannot be blurry or pixilated and must be perfectly square."
The artwork should probably contain something like "by Gavin Thorne" as well as the title.
VexaSonic make choose to make a CD version of the album, but I believe they use the .jpg file to generate that.

Thanks in advance,
Gavin :)

A mosaic, patchwork or collage would be good, to reflect the variety of the music.

I have added a couple of photos that you may or may not want to use. One is of me, the other is of my "studio", most of which is my laptop. :)

I hope that helps. (now you know why I haven't included these already)

Hi everyone

Thanks to all those who entered.

I received many suggestions, and the decision was tough.

Eventually I decided on "Quirk Jangle" as the name.
It is the name of one of the pieces on the album: http://tunehollow.net/thorneg/quirkjangle

Hopefully this will draw in the audience that will appreciate my quirky music.

The runners up were "Far Echoes" and "Dusk Lantern". Both of these two were submitted by Pixel Harbor participants.
I will organise a copy of the album to be sent to those people once the album comes out.

For background, the "Quirk" part of the name was from the musical concept of a mode, being an arrangement of a series of notes (scale). "Jangle" was my way of expressing a dismissive attitude to that - sort of like "Who needs conventional music theory".

Thanks again,
and good luck with the designs,
Gavin :)

Target Market(s)

People who buy music online. My music covers a wide range.

Industry/Entity Type

Online

```html
<!DOCTYPE html>
<html lang="en">
<head>
<meta charset="utf-8">
<title>Gavin Thorne – Quirk Jangle</title>
<link href="https://fonts.googleapis.com/css2?family=Mrs+Saint+Delafield&family=Libre+Caslon+Text&display=swap" rel="stylesheet">
<style>
  :root {
    --ink: #0d0d0f;
    --slate: #7e8090;
    --plum: #6c6c98;
    --plum-deep: #5a5a88;
    --rose: #a65a62;
    --gold: #c6a659;
    --cyan: #1db2e4;
    --teal: #2d97a9;
    --mint: #7db598;
    --sand: #c9bfac;
    --stone: #9b9ca3;
    --sky: #a9bedb;
    --cloud-light: #eef2f7;
    --cloud-mid: #bfcbdc;
  }
  html, body {
    margin: 0;
    padding: 0;
    overflow: hidden;
    background: #ffffff;
  }
  .cover {
    position: relative;
    width: 1200px;
    height: 1200px;
    overflow: hidden;
  }
  .mosaic {
    position: absolute;
    inset: 0;
    display: block;
  }
  .tile {
    stroke: var(--ink);
    stroke-width: 8;
    stroke-linejoin: round;
  }
  .seam {
    fill: none;
    stroke: var(--ink);
    stroke-width: 8;
    stroke-linecap: round;
    stroke-linejoin: round;
  }
  .artist-name,
  .album-title {
    position: absolute;
    left: 160px;
    width: 880px;
    margin: 0;
    text-align: center;
    color: var(--ink);
    font-weight: 400;
    white-space: nowrap;
  }
  .artist-name {
    top: 530px;
    font-family: "Mrs Saint Delafield", cursive;
    font-size: 155px;
    line-height: 155px;
    letter-spacing: 5px;
  }
  .album-title {
    top: 676px;
    font-family: "Libre Caslon Text", serif;
    font-size: 58px;
    line-height: 70px;
    letter-spacing: 1px;
  }
</style>
</head>
<body>
<main class="cover">
  <svg class="mosaic" viewBox="0 0 1200 1200" width="1200" height="1200">
    <defs>
      <linearGradient id="base-wash" x1="0" y1="0" x2="1" y2="1">
        <stop offset="0" stop-color="#8c8d9a"/>
        <stop offset="0.5" stop-color="#a3a5ad"/>
        <stop offset="1" stop-color="#7f8190"/>
      </linearGradient>
      <radialGradient id="cloud-wash" cx="0.5" cy="0.45" r="0.6">
        <stop offset="0" stop-color="var(--cloud-light)"/>
        <stop offset="1" stop-color="var(--cloud-mid)"/>
      </radialGradient>
    </defs>

    <rect class="backdrop" x="0" y="0" width="1200" height="1200" fill="url(#base-wash)"/>

    <!-- upper band -->
    <rect class="tile" x="-10" y="-10" width="330" height="170" rx="28" fill="var(--slate)"/>
    <rect class="tile" x="265" y="85" width="135" height="295" rx="28" fill="var(--sand)"/>
    <rect class="tile" x="320" y="85" width="80" height="120" rx="20" fill="var(--gold)"/>
    <path class="tile" d="M330 -10 H640 V85 Q640 100 655 100 H720 V235 H480 V200 H400 V-10 Z" fill="var(--rose)"/>
    <rect class="tile" x="480" y="-10" width="330" height="90" rx="24" fill="var(--stone)"/>
    <path class="tile" d="M720 85 H800 V160 H760 V240 H720 Z" fill="var(--teal)"/>
    <rect class="tile" x="760" y="80" width="200" height="170" rx="28" fill="#9b8f8a"/>
    <rect class="tile" x="800" y="-10" width="410" height="160" rx="28" fill="#8a97a8"/>
    <rect class="tile" x="1040" y="80" width="170" height="160" rx="28" fill="var(--gold)"/>
    <rect class="tile" x="1045" y="165" width="75" height="75" rx="16" fill="var(--cyan)"/>
    <rect class="tile" x="1120" y="240" width="90" height="50" rx="14" fill="var(--teal)"/>

    <!-- left staff band -->
    <rect class="tile" x="-10" y="160" width="330" height="160" rx="28" fill="var(--sand)"/>
    <rect class="tile" x="-10" y="235" width="320" height="40" rx="14" fill="var(--cyan)"/>
    <rect class="tile" x="-10" y="200" width="480" height="40" rx="14" fill="var(--plum)"/>
    <rect class="tile" x="330" y="200" width="150" height="40" rx="14" fill="var(--cyan)"/>
    <rect class="tile" x="265" y="300" width="140" height="90" rx="24" fill="#c8c8c8"/>

    <!-- middle band -->
    <rect class="tile" x="-10" y="320" width="400" height="240" rx="32" fill="var(--plum)"/>
    <rect class="tile" x="480" y="235" width="240" height="240" rx="32" fill="#b9b9b9"/>
    <rect class="tile" x="565" y="160" width="190" height="230" rx="28" fill="var(--mint)"/>
    <rect class="tile" x="565" y="160" width="100" height="90" rx="20" fill="#a8adb3"/>
    <path class="tile" d="M750 245 H880 V170 H960 V400 H800 V390 H750 Z" fill="var(--mint)"/>
    <rect class="tile" x="960" y="240" width="160" height="320" rx="28" fill="#9ea0a6"/>
    <rect class="tile" x="965" y="400" width="80" height="160" rx="20" fill="var(--sky)"/>
    <rect class="tile" x="1120" y="400" width="90" height="310" rx="24" fill="var(--gold)"/>

    <!-- lower band -->
    <rect class="tile" x="-10" y="560" width="250" height="280" rx="32" fill="var(--stone)"/>
    <rect class="tile" x="-10" y="720" width="80" height="80" rx="18" fill="var(--rose)"/>
    <path class="tile" d="M160 650 H1120 V860 H960 V1000 H560 V890 H400 V830 H160 Z" fill="var(--plum)"/>
    <rect class="tile" x="1040" y="800" width="170" height="300" rx="32" fill="var(--rose)"/>
    <rect class="tile" x="-10" y="860" width="420" height="260" rx="32" fill="var(--plum-deep)"/>
    <rect class="tile" x="-10" y="1005" width="265" height="40" rx="14" fill="var(--cyan)"/>
    <rect class="tile" x="330" y="830" width="400" height="190" rx="32" fill="var(--sand)"/>
    <rect class="tile" x="480" y="960" width="560" height="250" rx="32" fill="var(--plum)"/>
    <rect class="tile" x="880" y="880" width="160" height="330" rx="28" fill="#a0a1a8"/>
    <rect class="tile" x="960" y="960" width="250" height="250" rx="32" fill="#9a9ba1"/>
    <rect class="tile" x="180" y="1040" width="150" height="170" rx="28" fill="#a3a4ab"/>
    <rect class="tile" x="480" y="1120" width="320" height="90" rx="24" fill="#b4b5ba"/>
    <rect class="tile" x="725" y="1125" width="75" height="85" rx="16" fill="var(--teal)"/>

    <!-- long seam lines -->
    <path class="seam" d="M-10 160 H300 Q320 160 320 140 V100 Q320 80 340 80 H380 Q400 80 400 100 V220"/>
    <path class="seam" d="M-10 320 H250 Q270 320 270 340 V370 Q270 390 290 390 H380 Q400 390 400 370 V320 H570"/>
    <path class="seam" d="M-10 560 H60 Q80 560 80 580 V620 Q80 640 100 640 H220 Q240 640 240 660 V860 H-10"/>
    <path class="seam" d="M-10 920 H300 Q320 920 320 940 V980 Q320 1000 340 1000 H460 Q480 1000 480 1020 V1210"/>
    <path class="seam" d="M800 -10 V140 Q800 160 780 160 H760"/>
    <path class="seam" d="M1210 720 H1140 Q1120 720 1120 740 V800"/>

    <!-- central sky panel -->
    <path class="tile cloud-panel" role="img" aria-label="Soft cloudy sky photograph behind the album title"
      d="M190 490 H880 Q900 490 900 510 V560 Q900 575 915 575 H1020 Q1040 575 1040 595 V700 Q1040 720 1020 720 H900 Q880 720 880 740 V780 Q880 800 860 800 H640 Q620 800 620 820 V860 Q620 880 600 880 H580 Q560 880 560 860 V820 Q560 800 540 800 H340 Q320 800 320 780 V760 Q320 740 300 740 H180 Q160 740 160 720 V520 Q160 490 190 490 Z"
      fill="url(#cloud-wash)"/>
  </svg>

  <h1 class="artist-name">Gavin Thorne</h1>
  <h2 class="album-title">QUIRK JANGLE</h2>
</main>
</body>
</html>
```